Gantry Reclaim.com is wanting to create a Chatterloop Ad to attract buyers to come to their website. We are wanting buyers to register for free and create an account on Gantry Reclaim. com. We want to increase the number of buyers by posting an ad on Chatterloop groups. The buyer will click the link to our websites registration page.
https://www.gantryreclaim.com/account/users/register

Semi Trucks
Semi Trailers
Construction Equipment
Farm Equipment
Trailers
ATV/UTV
Boats
RVs

```html
<!DOCTYPE html>
<html lang="en">
<head>
<meta charset="utf-8">
<title>Gantry Reclaim – Unlock Deals on Heavy Equipment</title>
<link rel="stylesheet" href="https://fonts.googleapis.com/css2?family=Outfit:wght@400;500;700;800&display=swap">
<style>
  :root {
    --peach-edge: #fcd996;
    --peach-glow: #fff4d6;
    --ink: #111111;
    --orange: #e8632a;
    --white: #ffffff;
    --bar: #0d0d0d;
  }
  html, body {
    margin: 0;
    padding: 0;
    width: 1200px;
    height: 1200px;
    overflow: hidden;
    background: var(--peach-edge);
  }
  .ad {
    position: relative;
    width: 1200px;
    height: 1200px;
    overflow: hidden;
    font-family: "Outfit", sans-serif;
    color: var(--ink);
    background: radial-gradient(circle at 620px 160px, var(--peach-glow) 0%, #fee8b8 35%, var(--peach-edge) 80%);
  }
  .brand {
    position: absolute;
    top: 92px;
    right: 64px;
    display: flex;
    align-items: center;
    gap: 14px;
  }
  .brand-square {
    width: 34px;
    height: 34px;
    background: var(--orange);
  }
  .brand-name {
    font-weight: 800;
    font-size: 38px;
    line-height: 1;
    color: var(--ink);
    letter-spacing: 0.5px;
    text-transform: uppercase;
  }
  .photo-utv {
    position: absolute;
    z-index: 1;
    left: 640px;
    top: 312px;
    width: 490px;
    height: 530px;
    border-radius: 46% 46% 30% 30%;
    background: radial-gradient(ellipse at 50% 45%, #4c5a63 0%, #3d4a4c 45%, #5a6b52 70%, rgba(90,107,82,0) 100%);
  }
  .headline {
    position: absolute;
    z-index: 2;
    left: 86px;
    top: 286px;
    margin: 0;
    font-weight: 800;
    font-size: 102px;
    line-height: 94px;
    letter-spacing: -2px;
    text-transform: uppercase;
    white-space: nowrap;
  }
  .headline .accent { color: var(--orange); display: block; }
  .headline .dark { display: block; }
  .pitch {
    position: absolute;
    z-index: 2;
    left: 88px;
    top: 682px;
    margin: 0;
    font-size: 27px;
    line-height: 42px;
    font-weight: 400;
  }
  .pitch strong {
    display: block;
    font-size: 41px;
    font-weight: 700;
    line-height: 52px;
  }
  .cta-bar {
    position: absolute;
    left: 87px;
    top: 984px;
    width: 760px;
    height: 95px;
    border-radius: 16px;
    background: var(--bar);
  }
  .cta-button {
    position: absolute;
    left: 130px;
    top: 1006px;
    width: 332px;
    height: 52px;
    border-radius: 8px;
    background: var(--orange);
    color: var(--ink);
    font-weight: 700;
    font-size: 33px;
    display: flex;
    align-items: center;
    justify-content: center;
    gap: 14px;
    text-decoration: none;
    text-transform: uppercase;
  }
  .cta-button svg { width: 22px; height: 22px; }
  .contact {
    position: absolute;
    left: 520px;
    top: 1002px;
  }
  .contact-phone {
    color: var(--orange);
    font-weight: 700;
    font-size: 34px;
    line-height: 38px;
    display: block;
  }
  .contact-web {
    color: var(--white);
    font-size: 16px;
    line-height: 22px;
    display: block;
  }
  .photo-truck {
    position: absolute;
    left: 818px;
    top: 906px;
    width: 290px;
    height: 290px;
    border-radius: 50%;
    background: linear-gradient(180deg, #bcd3e6 0%, #e9eef0 40%, #d6d8d6 65%, #6d7a5c 100%);
  }
</style>
</head>
<body>
  <main class="ad">
    <div class="brand">
      <span class="brand-square"></span>
      <span class="brand-name">Gantry Reclaim</span>
    </div>

    <div class="photo-utv" role="img" aria-label="Photo of a green and dark grey side-by-side UTV facing forward"></div>

    <h1 class="headline">
      <span class="dark">Unlock</span>
      <span class="dark">Deals on</span>
      <span class="accent">Heavy</span>
      <span class="accent">Equipment</span>
    </h1>

    <p class="pitch">
      Looking for great deals
      <strong>Register for FREE</strong>
      on Gantry Reclaim and get access<br>
      to exclusive listings.
    </p>

    <div class="cta-bar"></div>
    <a class="cta-button" href="https://www.gantryreclaim.com/account/users/register">
      <svg viewBox="0 0 24 24" aria-hidden="true"><path d="M3 12h16M13 5l7 7-7 7" fill="none" stroke="#111" stroke-width="3" stroke-linecap="round" stroke-linejoin="round"/></svg>
      Sign Up Now
    </a>
    <div class="contact">
      <span class="contact-phone">(555) 214-0198</span>
      <span class="contact-web">https://www.gantryreclaim.com/</span>
    </div>

    <div class="photo-truck" role="img" aria-label="Photo of a white semi truck cab parked outdoors"></div>
  </main>
</body>
</html>
```